Northvale Coaching Company requires banner design

I need 3 large banners designed. i will be using these for advertising and also a condensed version as the header on a splash pages.

I have attached the wording and also the photo's that i'd like used in each design.
Note: i've just placed the wording randomly, you'll have to place it where it makes the most sense for the message and the design.

I want something with bright colors that pops.

Reason: I'd like to give the most recent designers time to submit quality work.

```html
<!DOCTYPE html>
<html lang="en">
<head>
<meta charset="utf-8">
<title>Northvale Coaching Company – Change Your Tomorrow Today</title>
<link rel="stylesheet" href="https://fonts.googleapis.com/css2?family=Anton&family=Open+Sans:wght@700&family=PT+Sans+Narrow&display=swap">
<style>
  :root {
    --ink: #000000;
    --paper: #ffffff;
    --alert-red: #ff1a1a;
    --accent-yellow: #f2d800;
    --band-text: #1c1a00;
    --mark-red-a: #e8483c;
    --mark-red-b: #5a1410;
    --photo-a: #3a2a22;
    --photo-b: #15100d;
  }
  html, body {
    margin: 0;
    padding: 0;
    overflow: hidden;
    background: var(--ink);
  }
  .banner {
    position: relative;
    width: 1200px;
    height: 360px;
    overflow: hidden;
    background: var(--ink);
    color: var(--paper);
    font-family: "PT Sans Narrow", "Arial Narrow", sans-serif;
  }
  .slogan-mark {
    position: absolute;
    left: 10px;
    top: 6px;
    width: 160px;
    height: 128px;
    border-radius: 10px;
    background: radial-gradient(circle at 40% 55%, var(--mark-red-a), var(--mark-red-b) 80%);
  }
  .headline {
    position: absolute;
    left: 218px;
    top: 26px;
    margin: 0;
    font-family: "Open Sans", Arial, sans-serif;
    font-weight: 700;
    line-height: 1;
  }
  .headline-main {
    display: block;
    font-size: 36px;
    letter-spacing: -0.5px;
  }
  .headline-sub {
    display: block;
    margin-top: 26px;
    margin-left: -4px;
    font-size: 21px;
    letter-spacing: -0.3px;
  }
  .headline-sub em {
    font-style: normal;
    color: var(--accent-yellow);
  }
  .call-to-action {
    position: absolute;
    left: 481px;
    top: 38px;
    margin: 0;
    font-family: "Anton", Impact, sans-serif;
    font-size: 52px;
    line-height: 1;
    letter-spacing: 0.5px;
    color: var(--alert-red);
    text-decoration: none;
    z-index: 2;
  }
  .pitch {
    position: absolute;
    left: 0;
    width: 1020px;
    margin: 0;
    text-align: center;
    font-size: 30px;
    line-height: 1;
    white-space: nowrap;
    z-index: 2;
  }
  .pitch-line-1 { top: 144px; }
  .pitch-line-2 { top: 182px; }
  .pitch-line-3 {
    top: 222px;
    width: 994px;
    font-size: 29px;
  }
  .pitch-line-3 strong {
    font-weight: 400;
    font-size: 46px;
  }
  .benefit-band {
    position: absolute;
    left: 0;
    top: 292px;
    width: 1200px;
    height: 32px;
    margin: 0;
    padding: 0;
    list-style: none;
    background: var(--accent-yellow);
  }
  .benefit-band li {
    position: absolute;
    top: 0;
    font-size: 29px;
    line-height: 32px;
    white-space: nowrap;
    color: var(--band-text);
  }
  .photo-couple {
    position: absolute;
    right: 0;
    top: 0;
    width: 330px;
    height: 360px;
    z-index: 1;
    background:
      linear-gradient(90deg, var(--ink) 0%, rgba(0,0,0,0) 25%),
      radial-gradient(ellipse at 55% 45%, var(--photo-a), var(--photo-b) 75%);
  }
</style>
</head>
<body>
  <main class="banner">
    <div class="slogan-mark" role="img" aria-label="Hand-lettered 'yes you can!' slogan with a pointing fist"></div>

    <h1 class="headline">
      <span class="headline-main">Change Your</span>
      <span class="headline-sub">Tomorrow – <em>TODAY!</em></span>
    </h1>

    <a class="call-to-action" href="#">FREE INFO CLICK HERE</a>

    <p class="pitch pitch-line-1">Learn to turn your spare time into an executive level income.</p>
    <p class="pitch pitch-line-2">In just 2 hours per day you can make a quantum leap in your results.</p>
    <p class="pitch pitch-line-3">Learn our success formula <strong>today</strong> so you can enjoy more <strong>tomorrow</strong></p>

    <ul class="benefit-band">
      <li style="left:100px">more time</li>
      <li style="left:278px">more fulfillment</li>
      <li style="left:543px">more money</li>
      <li style="left:770px">more fun</li>
    </ul>

    <div class="photo-couple" role="img" aria-label="Photo of a smiling couple posing together at night"></div>
  </main>
</body>
</html>
```